Dental Office Business Card

We need a business card for our pediatric dentistry office.
On one side the design needs to contain the following:
our logo (attached)
Vento Pediatric Grins
Soraya Kadbelani, DDS
Board Certified Pediatric Dentist
Tel: (555) 318-2747)
Fax: (555) 264-8031
Email: info@ventopediatricgrins.example
Web: www.ventopediatricgrins.example
Address: 41 Brindle Ave, Suite 208, Wellesley, MA 02099

On the other side of the card, the design needs to have an appointment reminder (date and time as well as day of the week) similar to the design attached (no need for appointment reason “For”)

```html
<!DOCTYPE html>
<html lang="en">
<head>
<meta charset="utf-8">
<title>Vento Pediatric Grins – Business Card</title>
<link rel="stylesheet" href="https://fonts.googleapis.com/css2?family=Montserrat:wght@400;500;700&display=swap">
<style>
  :root {
    --mint: #a7d7a9;
    --ink: #231f20;
    --paper: #ffffff;
    --backdrop: #f1eff0;
    --box: #a7d7a9;
  }
  * { margin: 0; padding: 0; box-sizing: border-box; }
  html, body { width: 1200px; height: 716px; overflow: hidden; }
  body {
    background: var(--backdrop);
    font-family: "Montserrat", sans-serif;
    color: var(--ink);
    position: relative;
  }
  .card {
    position: absolute;
    left: 369px;
    width: 461px;
    height: 264px;
    background: var(--paper);
    border-radius: 12px;
    overflow: hidden;
    box-shadow: 0 1px 4px rgba(0,0,0,0.12);
  }
  .card--reminder { top: 94px; }
  .card--contact { top: 385px; }

  .brand {
    position: absolute;
    display: flex;
    align-items: center;
    gap: 10px;
    font-weight: 700;
    color: var(--ink);
  }
  .brand__dot { border-radius: 50%; background: var(--mint); flex: none; }
  .card--reminder .brand { left: 0; right: 0; top: 36px; justify-content: center; font-size: 27px; white-space: nowrap; }
  .card--reminder .brand__dot { width: 36px; height: 36px; }
  .card--contact .brand { left: 17px; top: 24px; width: 200px; gap: 8px; font-size: 19px; line-height: 1.15; }
  .card--contact .brand__dot { width: 28px; height: 28px; }

  .field { position: absolute; left: 25px; font-size: 16px; display: flex; align-items: flex-end; }
  .field__line { border-bottom: 1.5px solid var(--ink); margin-left: 5px; height: 14px; }
  .field--date { top: 144px; }
  .field--date .field__line { width: 362px; }
  .field--time { top: 208px; }
  .field--time .field__line { width: 95px; }
  .meridiem { position: absolute; left: 196px; top: 210px; font-size: 17px; word-spacing: 8px; }

  .weekdays {
    position: absolute; left: 25px; top: 175px;
    display: flex; gap: 8px; list-style: none; font-size: 18px;
  }
  .weekdays li { display: flex; align-items: center; gap: 5px; }
  .weekdays li::before {
    content: ""; width: 12px; height: 12px; border: 1.5px solid var(--box);
  }
  .band--mint { position: absolute; left: 0; right: 0; bottom: 0; height: 18px; background: var(--mint); }

  .dentist { position: absolute; right: 17px; top: 40px; text-align: right; white-space: nowrap; }
  .dentist__name { color: var(--mint); font-weight: 700; font-size: 15.5px; }
  .dentist__title { font-size: 11.5px; font-weight: 500; margin-top: 3px; }
  .dentist-marker { position: absolute; right: 0; top: 42px; width: 7px; height: 28px; background: var(--mint); }

  .address { position: absolute; left: 17px; top: 114px; font-size: 12px; line-height: 17px; font-style: normal; font-weight: 500; }
  .contacts { position: absolute; left: 17px; top: 158px; list-style: none; font-size: 12px; line-height: 16.5px; font-weight: 500; }
  .contacts li { display: flex; align-items: center; gap: 3px; }
  .contacts svg { width: 10px; height: 10px; fill: var(--mint); flex: none; }

  .footer-bands { position: absolute; left: 0; bottom: 0; width: 461px; height: 27px; }
</style>
</head>
<body>

<section class="card card--reminder" aria-label="Appointment reminder">
  <div class="brand"><span class="brand__dot"></span>Vento Pediatric Grins</div>
  <div class="field field--date">Date :<span class="field__line"></span></div>
  <ul class="weekdays">
    <li>Mon</li><li>Tue</li><li>Wed</li><li>Thu</li><li>Fri</li><li>Sat</li><li>Sun</li>
  </ul>
  <div class="field field--time">Time :<span class="field__line"></span></div>
  <div class="meridiem">a.m p.m</div>
  <div class="band--mint"></div>
</section>

<section class="card card--contact" aria-label="Contact details">
  <div class="brand"><span class="brand__dot"></span><span>Vento Pediatric<br>Grins</span></div>
  <div class="dentist">
    <p class="dentist__name">Soraya Kadbelani, DDS</p>
    <p class="dentist__title">Board Certified Pediatric Dentist</p>
  </div>
  <div class="dentist-marker"></div>
  <address class="address">41 Brindle Ave, Suite 208,<br>Wellesley, MA 02099</address>
  <ul class="contacts">
    <li><svg viewBox="0 0 10 10"><path d="M1 4 C1 1 9 1 9 4 L7 4 L7 3 L3 3 L3 4 Z M2 5 L8 5 L9 9 L1 9 Z"/></svg>(555) 318-2747)</li>
    <li><svg viewBox="0 0 10 10"><rect x="3" y="0.5" width="4" height="3"/><rect x="0.5" y="3.5" width="9" height="4"/><rect x="3" y="6" width="4" height="3.5"/></svg>(555) 264-8031</li>
    <li><svg viewBox="0 0 10 10"><path d="M0.5 2 L9.5 2 L5 5.5 Z M0.5 3 L5 6.5 L9.5 3 L9.5 8 L0.5 8 Z"/></svg>info@ventopediatricgrins.example</li>
    <li><svg viewBox="0 0 10 10"><circle cx="5" cy="5" r="4.5"/></svg>www.ventopediatricgrins.example</li>
  </ul>
  <svg class="footer-bands" viewBox="0 0 461 27" preserveAspectRatio="none" aria-hidden="true">
    <polygon points="0,0 161,0 185,27 0,27" fill="var(--mint)"/>
    <polygon points="170,10 461,10 461,27 186,27" fill="var(--ink)"/>
  </svg>
</section>

</body>
</html>
```